SaaS Early tech startup business card design

Unique design for experience ecommerce platform company. the business cards will be used by executive members. conformance with color code is required.

```html
<!DOCTYPE html>
<html lang="en">
<head>
<meta charset="utf-8">
<title>nuvio business card</title>
<link rel="stylesheet" href="https://fonts.googleapis.com/css2?family=Roboto:wght@300;400;700;900&display=swap">
<style>
  :root {
    --backdrop: #6b6768;
    --card: #1f2139;
    --logo-grey: #8c8c92;
    --teal: #1fa39a;
    --text-light: #f2f2f4;
  }
  * { margin: 0; padding: 0; box-sizing: border-box; }
  html, body {
    width: 1200px; height: 1200px; overflow: hidden;
    background: var(--backdrop);
    font-family: "Roboto", Arial, sans-serif;
  }
  .card {
    position: absolute;
    width: 594px; height: 349px;
    background: var(--card);
    border-radius: 20px;
  }
  .card--front { left: 299px; top: 198px; }
  .card--back { left: 292px; top: 636px; }

  .front-wordmark {
    position: absolute; left: 0; right: 0; top: 72px;
    text-align: center;
    font-weight: 900; font-size: 150px; line-height: 1;
    letter-spacing: -2px;
    color: var(--logo-grey);
  }
  .front-tagline {
    position: absolute; left: 0; right: 0; top: 245px;
    text-align: center;
    font-weight: 300; font-size: 17px;
    letter-spacing: 0.42em; padding-left: 0.42em;
    color: var(--text-light);
  }

  .holder-name {
    position: absolute; left: 65px; top: 80px;
    font-weight: 700; font-size: 24px; color: var(--teal);
    letter-spacing: -0.3px;
  }
  .holder-role {
    position: absolute; left: 65px; top: 106px;
    font-size: 17px; color: var(--text-light);
  }
  .contact-list {
    position: absolute; left: 73px; top: 152px;
    list-style: none;
  }
  .contact-list li {
    display: flex; align-items: center;
    height: 22px; font-size: 16.5px; color: var(--text-light);
  }
  .contact-list svg { width: 14px; height: 14px; margin-right: 18px; fill: var(--teal); }
  .address {
    position: absolute; left: 65px; top: 226px;
    font-size: 16.5px; line-height: 22px; color: var(--text-light);
  }
  .back-wordmark {
    position: absolute; left: 291px; top: 122px; width: 232px;
    text-align: center;
    font-weight: 900; font-size: 80px; line-height: 1;
    letter-spacing: -1px;
    color: var(--teal);
  }
  .back-tagline {
    position: absolute; left: 291px; top: 204px; width: 232px;
    text-align: center;
    font-weight: 400; font-size: 12.5px;
    letter-spacing: 0.42em; padding-left: 0.42em;
    color: var(--teal);
  }
</style>
</head>
<body>
  <section class="card card--front">
    <div class="front-wordmark">nuvio</div>
    <div class="front-tagline">BUILT AROUND YOU</div>
  </section>

  <section class="card card--back">
    <div class="holder-name">Darin K.</div>
    <div class="holder-role">CTO/Owner</div>
    <ul class="contact-list">
      <li>
        <svg viewBox="0 0 14 14" aria-hidden="true"><path d="M1 5c0-2 2-3 6-3s6 1 6 3v1h-3V5H4v1H1zM3 7h8l1.5 5h-11z"/></svg>
        (00) 0111 NUVIO
      </li>
      <li>
        <svg viewBox="0 0 14 14" aria-hidden="true"><path d="M1 3h12v8H1zm1 1v.3l5 3.5 5-3.5V4z"/></svg>
        info@nuvio.net
      </li>
      <li>
        <svg viewBox="0 0 14 14" aria-hidden="true"><path d="M7 1a6 6 0 1 0 0 12A6 6 0 0 0 7 1zm0 1.2c.8.8 1.4 2.3 1.5 4.2h-3C5.6 4.5 6.2 3 7 2.2zM2.3 6.4a4.8 4.8 0 0 1 2.6-3.7c-.5 1-.8 2.300-.9 3.7zm0 1.2H4c.1 1.4.4 2.7.9 3.7a4.8 4.8 0 0 1-2.6-3.7zM7 11.8c-.8-.8-1.4-2.3-1.5-4.2h3c-.1 1.9-.7 3.4-1.5 4.2zm2.1-.5c.5-1 .8-2.3.9-3.7h1.7a4.8 4.8 0 0 1-2.6 3.7zM10 6.4c-.1-1.4-.4-2.7-.9-3.7a4.8 4.8 0 0 1 2.6 3.7z"/></svg>
        www.nuvio.net
      </li>
    </ul>
    <div class="address">Harbor Tower, Dubai<br>Creek Tech Quarter, UAE</div>
    <div class="back-wordmark">nuvio</div>
    <div class="back-tagline">BUILT AROUND YOU</div>
  </section>
</body>
</html>
```